Waterjet Cutting Business requires an up to date website

We currently have a website which is outdated and in need of modernization.
We are only looking for a simple website with around 4 pages: Home, Contact Us, Materials, Gallery.
We have some pictures and a logo which can be used.
Our primary business is profile cutting of materials to customers specifications using high-pressure water with abrasive.
We are looking for creative ideas and are open to suggestions!
http://brightfordcutworks.com/index.asp?pid=1
Update:
Cut quality picture (uploaded)
Map
Comparison to other profile cutting methods such as plasma/laser
Single page style without continuous scrolling
"We can cut virtually any material from any drawing whether it be a Full 3D cad models to hand sketched "
Target Market(s)
Film Industry, Prototype, Engineering, Architect, Artisits, one off designs
Industry/Entity Type
Engineering
Number of Pages Required
1 page
Font styles to use
Look and feel

```html
<!DOCTYPE html>
<html lang="en">
<head>
<meta charset="utf-8">
<title>Brightford Cutworks — Waterjet Cutting Service</title>
<link rel="stylesheet" href="https://fonts.googleapis.com/css2?family=Montserrat:wght@600&family=Open+Sans:ital,wght@0,400;0,800;1,600&display=swap">
<style>
  :root {
    --white: #ffffff;
    --ink-navy: #14133f;
    --deep-violet: #1b1248;
    --royal-blue: #2b3fb8;
    --electric-blue: #3d6fe0;
    --magenta: #c23a9a;
    --footer-band: #1d0f3c;
  }
  * { margin: 0; padding: 0; box-sizing: border-box; }
  html, body { width: 1200px; height: 702px; overflow: hidden; background: var(--ink-navy); }
  .page {
    position: relative;
    width: 1200px;
    height: 702px;
    overflow: hidden;
    color: var(--white);
    font-family: "Open Sans", Arial, sans-serif;
  }
  .hero-photo {
    position: absolute;
    inset: 0;
    background:
      radial-gradient(ellipse 420px 320px at 880px 190px, rgba(194,58,154,0.55), transparent 70%),
      radial-gradient(ellipse 520px 360px at 300px 260px, rgba(61,111,224,0.55), transparent 70%),
      linear-gradient(160deg, var(--royal-blue) 0%, #24309a 35%, var(--deep-violet) 75%, #120a30 100%);
  }
  .site-header {
    position: absolute;
    top: 0; left: 0; right: 0;
    height: 60px;
  }
  .brand {
    position: absolute;
    left: 33px;
    top: 20px;
    font-family: "Montserrat", Arial, sans-serif;
    font-weight: 600;
    font-size: 20px;
    letter-spacing: 1px;
    color: var(--white);
  }
  .main-nav a {
    position: absolute;
    top: 15px;
    font-family: "Montserrat", Arial, sans-serif;
    font-weight: 600;
    font-size: 18px;
    color: var(--white);
    text-decoration: none;
  }
  .nav-home { left: 594px; }
  .nav-materials { left: 719px; }
  .nav-gallery { left: 889px; }
  .nav-contact { left: 1043px; }
  .intro {
    position: absolute;
    left: 47px;
    top: 258px;
  }
  .intro-kicker {
    font-size: 19px;
    font-weight: 400;
    margin-bottom: 13px;
  }
  .intro-headline {
    font-size: 28.5px;
    font-weight: 800;
    line-height: 37.5px;
    letter-spacing: -0.8px;
    text-transform: uppercase;
  }
  .next-button {
    display: inline-block;
    margin-top: 22px;
    width: 97px;
    height: 32px;
    line-height: 32px;
    text-align: center;
    background: var(--white);
    color: var(--ink-navy);
    border-radius: 8px;
    font-family: "Montserrat", Arial, sans-serif;
    font-weight: 600;
    font-size: 15px;
    text-decoration: none;
  }
  .project-strip {
    position: absolute;
    left: 0;
    top: 525px;
  }
  .footer-band {
    position: absolute;
    left: 0; right: 0; bottom: 0;
    height: 20px;
    background: var(--footer-band);
  }
  .copyright {
    position: absolute;
    left: 51px;
    bottom: 4px;
    font-size: 10.5px;
    font-style: italic;
    font-weight: 600;
  }
</style>
</head>
<body>
<div class="page">
  <div class="hero-photo" role="img" aria-label="Close-up of a waterjet cutting head over a wet metal cutting bed, lit in blue and magenta"></div>

  <header class="site-header">
    <div class="brand">BRIGHTFORD CUTWORKS</div>
    <nav class="main-nav">
      <a class="nav-home" href="#">HOME</a>
      <a class="nav-materials" href="#">MATERIALS</a>
      <a class="nav-gallery" href="#">GALLERY</a>
      <a class="nav-contact" href="#">CONTACT US</a>
    </nav>
  </header>

  <section class="intro">
    <p class="intro-kicker">Waterjet Cutting Service</p>
    <h1 class="intro-headline">We can cut virtually<br>any material from any drawing<br>whether it be a full 3D CAD models<br>to hand sketched</h1>
    <a class="next-button" href="#">NEXT</a>
  </section>

  <svg class="project-strip" width="1200" height="157" viewBox="0 0 1200 157" role="img" aria-label="Four slanted photo panels of waterjet heads cutting metal with sparks">
    <defs>
      <linearGradient id="panel-gold" x1="0" y1="0" x2="1" y2="1">
        <stop offset="0" stop-color="#3a2a14"/><stop offset="0.5" stop-color="#8a6a3a"/><stop offset="1" stop-color="#4a1010"/>
      </linearGradient>
      <linearGradient id="panel-teal" x1="0" y1="0" x2="0" y2="1">
        <stop offset="0" stop-color="#0d1a1c"/><stop offset="1" stop-color="#1f9a86"/>
      </linearGradient>
      <linearGradient id="panel-pink" x1="0" y1="0" x2="1" y2="1">
        <stop offset="0" stop-color="#3a0a3a"/><stop offset="0.6" stop-color="#d23fc4"/><stop offset="1" stop-color="#6a1070"/>
      </linearGradient>
      <linearGradient id="panel-steel" x1="0" y1="0" x2="0" y2="1">
        <stop offset="0" stop-color="#b8b4b0"/><stop offset="0.5" stop-color="#6a5a56"/><stop offset="1" stop-color="#d8d6d4"/>
      </linearGradient>
    </defs>
    <polygon points="556,0 723,0 652,157 490,157" fill="url(#panel-gold)"/>
    <polygon points="723,0 882,0 811,157 652,157" fill="url(#panel-teal)"/>
    <polygon points="882,0 1045,0 979,157 811,157" fill="url(#panel-pink)"/>
    <polygon points="1045,0 1200,0 1200,157 979,157" fill="url(#panel-steel)"/>
  </svg>

  <footer class="footer-band">
    <p class="copyright">© Copyright&nbsp; 2018&nbsp; Brightford Cutworks&nbsp; All rights reserved.</p>
  </footer>
</div>
</body>
</html>
```